New Business Card Design Project

Use the flyer uploaded and website www.brightoakbuilders.com for inspiration.
List Our Services on Backside of business cards
Martin Hollis
Harborline Renovations Inc.
Licensed General Contractors
858-471-9063

Contact Information for Business Card

Use the flyer uploaded and website www.brightoakbuilders.com for inspiration. List Our Services on Backside of business cards Martin Hollis Harborline Renovations Inc. Licensed General Contractors 858-471-9063

```html
<!DOCTYPE html>
<html lang="en">
<head>
<meta charset="utf-8">
<title>Harborline Renovations – Business Card</title>
<link href="https://fonts.googleapis.com/css2?family=Marcellus&family=Raleway:wght@400;500&display=swap" rel="stylesheet">
<style>
  :root{
    --page:#dadada;
    --card:#060606;
    --band:#141414;
    --band-soft:#1b1b1b;
    --gold:#e3bf6c;
    --gold-line:#d9a64e;
  }
  *{margin:0;padding:0;box-sizing:border-box}
  html,body{width:1200px;height:1200px;overflow:hidden;background:var(--page)}
  .canvas{position:relative;width:1200px;height:1200px}
  .card{position:absolute;width:785px;height:462px;overflow:hidden;
    background:radial-gradient(ellipse at 60% 50%, #161616 0%, var(--card) 75%)}
  .card--front{left:121px;top:121px}
  .card--back{left:302px;top:624px}
  .card__art{position:absolute;inset:0;width:100%;height:100%}
  .holder-name{position:absolute;right:61px;top:70px;font-family:"Marcellus",serif;
    font-size:43px;letter-spacing:9px;color:var(--gold);white-space:nowrap;margin-right:-9px}
  .holder-title{position:absolute;right:61px;top:118px;font-family:"Raleway",sans-serif;
    font-size:23px;color:var(--gold);white-space:nowrap}
  .contact{position:absolute;right:96px;font-family:"Raleway",sans-serif;font-size:20px;
    color:var(--gold);text-align:right;white-space:nowrap;line-height:29px}
  .contact--phone{top:193px;right:116px}
  .contact--web{top:243px;right:118px}
  .contact--mail{top:291px}
  .contact--address{top:340px}
  .icon{position:absolute;width:26px;height:26px;left:698px}
  .brand{position:absolute;font-family:"Marcellus",serif;color:var(--gold);
    white-space:nowrap;transform:translateX(-50%)}
  .brand--front{left:207px;top:248px;font-size:22px;letter-spacing:1px}
  .brand--back{left:392px;top:268px;font-size:36px;letter-spacing:2px}
</style>
</head>
<body>
<main class="canvas">

  <section class="card card--front" aria-label="Business card front">
    <svg class="card__art" viewBox="0 0 785 462" aria-hidden="true">
      <polygon points="0,100 78,0 192,0 0,248" fill="var(--band)"/>
      <polygon points="0,351 268,0 418,0 0,460" fill="var(--band-soft)"/>
      <polygon points="110,462 211,364 328,462" fill="var(--band)"/>
      <line x1="77" y1="0" x2="0" y2="98" stroke="var(--gold-line)" stroke-width="1.6"/>
      <line x1="192" y1="0" x2="0" y2="248" stroke="var(--gold-line)" stroke-width="1.6"/>
      <line x1="418" y1="0" x2="331" y2="114" stroke="var(--gold-line)" stroke-width="1.6"/>
      <line x1="67" y1="267" x2="0" y2="351" stroke="var(--gold-line)" stroke-width="1.6"/>
      <line x1="109" y1="404" x2="176" y2="461" stroke="var(--gold-line)" stroke-width="1.6"/>
      <line x1="211" y1="364" x2="328" y2="461" stroke="var(--gold-line)" stroke-width="1.6"/>
    </svg>

    <div class="brand brand--front">HARBORLINE RENOVATIONS</div>

    <h1 class="holder-name">MARTIN HOLLIS</h1>
    <p class="holder-title">Licensed General Contractors</p>

    <p class="contact contact--phone">858-471-9063</p>
    <svg class="icon" style="top:196px" viewBox="0 0 24 24" aria-hidden="true">
      <path d="M5 2h4l2 5-3 2c1.2 2.8 3.2 4.8 6 6l2-3 5 2v4c0 1.1-.9 2-2 2C10 20 4 14 3 4c0-1.1.9-2 2-2z" fill="var(--gold)"/>
    </svg>

    <p class="contact contact--web">www.brightoakbuilders.com</p>
    <svg class="icon" style="top:245px" viewBox="0 0 24 24" aria-hidden="true">
      <g fill="none" stroke="var(--gold)" stroke-width="1.6">
        <circle cx="12" cy="12" r="10.5"/>
        <ellipse cx="12" cy="12" rx="4.5" ry="10.5"/>
        <line x1="1.5" y1="12" x2="22.5" y2="12"/>
        <line x1="3.5" y1="7" x2="20.5" y2="7"/>
        <line x1="3.5" y1="17" x2="20.5" y2="17"/>
      </g>
    </svg>

    <p class="contact contact--mail">office@harborlinereno.com</p>
    <svg class="icon" style="top:295px" viewBox="0 0 24 24" aria-hidden="true">
      <rect x="1" y="4" width="22" height="16" fill="var(--gold)"/>
      <polyline points="1,5 12,13 23,5" fill="none" stroke="var(--card)" stroke-width="1.8"/>
    </svg>

    <p class="contact contact--address">L1: 14 Fenwick Yard, London, EC3A 2BN<br>L2: 41 Marlowe St, London, N4 2QT</p>
    <svg class="icon" style="top:355px;height:32px" viewBox="0 0 24 30" aria-hidden="true">
      <path d="M12 1C6.5 1 3 5 3 10c0 6 9 19 9 19s9-13 9-19c0-5-3.5-9-9-9z" fill="var(--gold)"/>
      <circle cx="12" cy="10" r="3.3" fill="var(--card)"/>
    </svg>
  </section>

  <section class="card card--back" aria-label="Business card back">
    <svg class="card__art" viewBox="0 0 785 462" aria-hidden="true">
      <polygon points="0,116 98,244 0,244" fill="var(--band)"/>
      <polygon points="0,190 216,462 94,462 0,330" fill="var(--band-soft)"/>
      <polygon points="560,0 634,0 785,190 785,300" fill="var(--band)"/>
      <polygon points="680,0 745,0 785,51 785,140" fill="var(--band-soft)"/>
      <line x1="0" y1="116" x2="98" y2="244" stroke="var(--gold-line)" stroke-width="1.6"/>
      <line x1="0" y1="276" x2="94" y2="461" stroke="var(--gold-line)" stroke-width="1.6"/>
      <line x1="110" y1="332" x2="216" y2="462" stroke="var(--gold-line)" stroke-width="1.6"/>
      <line x1="634" y1="0" x2="701" y2="82" stroke="var(--gold-line)" stroke-width="1.6"/>
      <line x1="745" y1="0" x2="785" y2="51" stroke="var(--gold-line)" stroke-width="1.6"/>
      <line x1="729" y1="63" x2="785" y2="135" stroke="var(--gold-line)" stroke-width="1.6"/>
      <line x1="661" y1="138" x2="785" y2="301" stroke="var(--gold-line)" stroke-width="1.6"/>
    </svg>

    <div class="brand brand--back">HARBORLINE RENOVATIONS</div>
  </section>

</main>
</body>
</html>
```